Hockey Youth Club - Complete HP Design

I need a complete homepage design for a new youth hockey club. There are already some elements that can be used. For more information, please visit this products webpage. This site is currently unavailable for purchase at this time (Current) -) Team (Players, Coaches, Crew) -) Club (Philiosophy , Rules, Management Board, ....) -) Partners (Sponsors, Partners, ...)) Contact (Contact details, Callback Button) -) Shop (in the beginning view of products - further planned as online shop ) -) .... probably 2-3 more -) Footer with social media info, ..... Homepages from other youth hockey clubs (ex. Www.brel. At - this is what I am looking for in my life - BUT we dont want to copy them !!! Im interested in new and innovative designs.
Updates

Project Deadline Extended
Reason: Too much Wordpress - no innovation - please offer more designs in dark concept. At the moment the design is too decent - we are looking for sporty, active and fresh design. Thank you

Target Market(s)

Youth Hockey Players Parents

Industry/Entity Type

Club

Number of Pages Required

5+ page

Colors
fbed38
9d9d9d
1b1b1b
f5f5f5
ffffff

Requirements
Must have
• Clearline, modern design,
Nice to have
• Flashing elements (maybe the scratches fading in ...)
Should not have
• chaos

```html
<!DOCTYPE html>
<html lang="en">
<head>
<meta charset="utf-8">
<title>Hornets Hockey Youth Club</title>
<link href="https://fonts.googleapis.com/css2?family=Graduate&family=Oswald:wght@400;500;600;700&family=Lato:ital,wght@0,400;0,700;1,400&display=swap" rel="stylesheet">
<style>
:root{
  --yellow:#fbc52d;
  --yellow-light:#fbed38;
  --grey:#9d9d9d;
  --dark:#1b1b1b;
  --panel:#232323;
  --light:#f5f5f5;
  --white:#ffffff;
  --text:#555555;
}
*{box-sizing:border-box;margin:0;padding:0}
html,body{width:1200px;height:3352px;overflow:hidden}
body{position:relative;background:var(--white);font-family:"Lato",sans-serif;color:var(--dark)}
.abs{position:absolute}
.heading{font-family:"Graduate",serif;font-size:38px;letter-spacing:1px;color:var(--dark);text-transform:uppercase;white-space:nowrap}
.heading .hl{color:var(--yellow);text-shadow:2px 2px 0 var(--dark)}

/* top bar */
.topbar{left:0;top:0;width:1200px;height:40px;background:var(--dark);color:var(--white);font-size:12px}
.topbar .breaking{left:98px;top:12px;font-family:"Oswald",sans-serif;font-weight:600}
.topbar .breaking span{color:var(--yellow)}
.topbar .ticker{left:232px;top:13px;font-size:11px;color:#ddd}
.topbar .social{left:800px;top:11px;display:flex;gap:10px}
.dot{width:18px;height:18px;border-radius:50%;background:var(--yellow)}
.topbar .cart{left:1000px;top:11px;font-family:"Oswald",sans-serif;font-weight:600;display:flex;align-items:center;gap:6px}
.badge{width:16px;height:16px;border-radius:50%;background:var(--yellow);color:var(--dark);font-size:10px;text-align:center;line-height:16px}

/* hero */
.hero{left:0;top:40px;width:1200px;height:695px;background:linear-gradient(90deg,#eeeeee 0%,#f6f6f6 45%,#f3f3f3 60%,var(--yellow) 70%,#fcc52a 100%);overflow:hidden}
.hero .decor{right:0;top:0;width:420px;height:695px;background:radial-gradient(circle at 60% 45%,#ffd457 0%,#fbbf22 60%,#f6b216 100%)}
.hero .player{left:440px;top:90px;width:420px;height:600px;border-radius:40% 40% 10% 10%;background:linear-gradient(180deg,#2b3140 0%,#c8ccd4 35%,#e7e9ee 55%,#3a3f4b 80%,#1f232b 100%);opacity:.92}
.logo{left:98px;top:62px;display:flex;align-items:center;gap:10px}
.logo .mark{width:40px;height:40px;background:var(--yellow)}
.logo .name{font-family:"Graduate",serif;font-size:44px;color:var(--dark)}
.nav{left:396px;top:57px;width:710px;height:60px;background:var(--dark);display:flex;align-items:center;padding-left:22px;gap:27px;font-family:"Oswald",sans-serif;font-weight:600;font-size:16px;color:var(--white)}
.nav svg{margin-left:auto;margin-right:22px}
.welcome{left:112px;top:232px;font-family:"Graduate",serif;font-size:50px;font-weight:400;color:var(--dark)}
.club-title{left:98px;top:290px;font-family:"Graduate",serif;font-size:96px;line-height:1;color:var(--yellow);text-shadow:4px 4px 0 var(--dark)}
.club-sub{left:98px;top:395px;width:380px;height:42px;background:var(--dark);color:var(--yellow);font-family:"Graduate",serif;font-size:28px;line-height:42px;text-align:center}
.btn-more{left:98px;top:468px;width:162px;height:38px;background:var(--yellow);display:flex;align-items:center;font-family:"Oswald",sans-serif;font-weight:600;font-size:15px;color:var(--dark)}
.btn-more span{padding-left:12px;flex:1}
.btn-more i{width:38px;height:38px;background:var(--dark);display:flex;align-items:center;justify-content:center}
.hero-dots{left:98px;top:550px;display:flex;gap:10px}
.hero-dots b{width:8px;height:8px;background:var(--yellow);transform:rotate(45deg)}

/* team */
.team-title{left:98px;top:760px}
.arrows{left:1054px;top:772px;display:flex;gap:6px}
.arrows i{width:20px;height:20px;border:2px solid var(--grey);border-radius:50%}
.card{top:832px;width:232px;height:320px;background:var(--yellow);overflow:hidden}
.card .photo{left:40px;top:0;width:192px;height:320px}
.card .name{left:0;top:0;width:40px;height:260px;writing-mode:vertical-rl;transform:rotate(180deg);display:flex;align-items:center;justify-content:flex-start;padding:0 8px;font-family:"Oswald",sans-serif;font-weight:700;font-size:20px;color:var(--dark)}
.card .role{font-size:13px;font-weight:500;margin-bottom:12px}
.card .num{left:0;top:278px;width:40px;text-align:center;font-family:"Oswald",sans-serif;font-weight:700;font-size:22px}

/* stats */
.stats{left:0;top:1210px;width:1200px;height:200px;background:linear-gradient(180deg,#fbb91d,#fccb35);clip-path:polygon(0 0,100% 0,100% 94%,90% 100%,78% 95%,62% 100%,45% 94%,28% 100%,14% 95%,0 100%)}
.stat{top:60px;display:flex;align-items:center;gap:14px}
.stat b{display:block;font-family:"Oswald",sans-serif;font-size:46px;font-weight:600;line-height:1}
.stat span{font-family:"Oswald",sans-serif;font-size:17px;text-transform:uppercase}

/* products */
.prod-title{left:0;top:1468px;width:1200px;text-align:center}
.underline{width:110px;height:3px;background:var(--yellow);margin:10px auto 0}
.prod-text{left:240px;top:1555px;width:720px;text-align:center;font-size:12px;line-height:20px;color:var(--text)}
.product{top:1622px;width:232px;height:385px}
.product .img{left:0;top:0;width:232px;height:282px;background:linear-gradient(180deg,#e2e2e2,#f4f4f4)}
.product .pname{left:0;top:282px;width:232px;height:48px;background:var(--white);border:3px solid var(--dark);display:flex;align-items:center;justify-content:center;font-family:"Graduate",serif;font-size:22px;color:var(--yellow);text-shadow:1px 1px 0 var(--dark)}
.product .bar{left:0;top:330px;width:232px;height:42px;background:var(--panel);color:var(--white);display:flex;align-items:center;justify-content:space-between;padding:0 18px;font-family:"Oswald",sans-serif;font-weight:600;font-size:15px}
.product .bar .price{color:var(--yellow)}

/* partners */
.partners{left:0;top:2057px;width:1200px;height:390px;background:linear-gradient(180deg,#e9e9e9,#f5f5f5)}
.partners .heading{position:absolute;left:0;top:50px;width:1200px;text-align:center}
.partners .sub{position:absolute;left:0;top:100px;width:1200px;text-align:center;font-style:italic;font-size:22px;color:var(--grey)}
.partners .underline{position:absolute;left:545px;top:138px;margin:0}
.plogo{top:172px;width:160px;height:80px;background:var(--white);box-shadow:0 2px 6px rgba(0,0,0,.12);display:flex;align-items:center;justify-content:center;font-style:italic;font-size:22px;color:var(--dark)}
.partners .hero-dots{left:572px;top:290px}

/* news */
.news-title{left:0;top:2395px;width:1200px;text-align:center}
.news-main{left:98px;top:2490px;width:500px;height:270px;background:linear-gradient(160deg,#2d3a24,#6f8a4c 45%,#243045 75%,#1c1c1c)}
.date{font-family:"Oswald",sans-serif;font-size:14px;color:var(--yellow);text-transform:uppercase}
.ntitle{font-family:"Oswald",sans-serif;font-size:20px;font-weight:500;color:var(--dark);white-space:nowrap}
.meta{display:flex;gap:22px;font-size:12px;color:var(--text);align-items:center}
.news-item{left:625px;width:480px;height:120px;border-bottom:1px solid #ddd}
.news-item .thumb{left:0;top:0;width:122px;height:88px;background:linear-gradient(160deg,#2d3a24,#6f8a4c 50%,#243045)}
.news-item .txt{left:137px;top:0}

/* footer */
.footer{left:0;top:2975px;width:1200px;height:377px;background:var(--panel);clip-path:polygon(0 6%,6% 2%,14% 7%,24% 1%,35% 6%,47% 0,58% 5%,70% 1%,82% 6%,92% 2%,100% 5%,100% 100%,0 100%)}
.footer .name{left:168px;top:118px;font-family:"Graduate",serif;font-size:34px;color:var(--yellow)}
.f-about{left:168px;top:170px;width:200px;font-size:10px;line-height:16px;color:#bbb}
.f-col h4{font-family:"Oswald",sans-serif;font-size:13px;color:var(--white);margin-bottom:14px}
.f-col h4 span{color:var(--yellow)}
.f-col li{list-style:none;font-size:10px;line-height:17px;color:#bbb}
.f-col .bul li::before{content:"";display:inline-block;width:5px;height:5px;background:var(--yellow);margin-right:10px;vertical-align:middle}
.contact li{display:flex;gap:8px;align-items:center;margin-bottom:6px}
.f-social{left:850px;top:240px;display:flex;gap:10px}
.f-social .dot{width:24px;height:24px}
.copy{left:0;top:3282px;width:1200px;height:70px;background:var(--dark);color:#bbb;font-size:12px;text-align:center;line-height:70px}
</style>
</head>
<body>

<header class="abs topbar">
  <div class="abs breaking">BREAKING <span>NEWS</span></div>
  <div class="abs ticker">Spring tryouts open for all age groups this month.</div>
  <div class="abs social"><i class="dot"></i><i class="dot"></i><i class="dot"></i><i class="dot"></i></div>
  <div class="abs cart">
    <svg width="16" height="14" viewBox="0 0 16 14"><path d="M0 1h3l2 8h9l2-6H4" fill="none" stroke="#fbc52d" stroke-width="2"/><circle cx="6" cy="12" r="1.5" fill="#fbc52d"/><circle cx="13" cy="12" r="1.5" fill="#fbc52d"/></svg>
    CART <span class="badge">0</span>
  </div>
</header>

<section class="abs hero">
  <div class="abs decor" role="img" aria-label="Large faint club emblem decoration on yellow"></div>
  <div class="abs player" role="img" aria-label="Photo of a young hockey player skating with stick"></div>
  <div class="abs logo"><i class="mark"></i><span class="name">HORNETS</span></div>
  <nav class="abs nav">
    <span>HOME</span><span>NEWS</span><span>TEAM</span><span>CLUB</span><span>PARTNERS</span><span>CONTACT</span><span>SHOP</span>
    <svg width="20" height="20" viewBox="0 0 20 20"><circle cx="8" cy="8" r="6" fill="none" stroke="#fbc52d" stroke-width="2.5"/><path d="M13 13l5 5" stroke="#fbc52d" stroke-width="2.5"/></svg>
  </nav>
  <h1 class="abs welcome">WELCOME TO</h1>
  <div class="abs club-title">HORNETS</div>
  <div class="abs club-sub">HOCKEY YOUTH CLUB</div>
  <div class="abs btn-more"><span>READ MORE</span><i><svg width="16" height="14" viewBox="0 0 16 14"><path d="M0 7h13M8 2l5 5-5 5" fill="none" stroke="#fbc52d" stroke-width="2"/></svg></i></div>
  <div class="abs hero-dots"><b></b><b></b><b></b></div>
</section>

<section>
  <h2 class="abs heading team-title"><span class="hl">TEAM</span> MEMBER</h2>
  <div class="abs arrows"><i></i><i></i></div>
  <article class="abs card" style="left:98px">
    <div class="abs photo" role="img" aria-label="Photo of coach" style="background:linear-gradient(180deg,#7c8a6a,#3b3b3b 60%,#1d1d1d)"></div>
    <div class="abs name"><span class="role">COACH</span>OWEN HARTLEY</div><div class="abs num">12</div>
  </article>
  <article class="abs card" style="left:353px">
    <div class="abs photo" role="img" aria-label="Photo of player in action" style="background:linear-gradient(180deg,#6f7b5a,#2a3b70 50%,#3f5a2c)"></div>
    <div class="abs name"><span class="role">PLAYER</span>MILA TORRANCE</div><div class="abs num">10</div>
  </article>
  <article class="abs card" style="left:610px">
    <div class="abs photo" role="img" aria-label="Photo of player in helmet" style="background:linear-gradient(180deg,#9aa4b0,#2d4a9a 40%,#e8e8ee)"></div>
    <div class="abs name"><span class="role">PLAYER</span>REID CALLOWAY</div><div class="abs num">22</div>
  </article>
  <article class="abs card" style="left:866px">
    <div class="abs photo" role="img" aria-label="Photo of crew member" style="background:linear-gradient(180deg,#b8c2c8,#6a8499 50%,#3c5a78)"></div>
    <div class="abs name"><span class="role">CREW</span>JONAH PIERCE</div><div class="abs num">22</div>
  </article>
</section>

<section class="abs stats">
  <div class="abs stat" style="left:98px">
    <svg width="64" height="50" viewBox="0 0 64 50"><path d="M6 38C4 16 22 4 38 6c16 2 22 16 20 30H30v8H14z" fill="none" stroke="#1b1b1b" stroke-width="3"/><path d="M30 30h26" stroke="#1b1b1b" stroke-width="3"/></svg>
    <div><b>23</b><span>Matches Played</span></div>
  </div>
  <div class="abs stat" style="left:372px">
    <svg width="58" height="50" viewBox="0 0 58 50"><path d="M6 4l30 38h14M52 4L22 42H8" fill="none" stroke="#1b1b1b" stroke-width="3"/></svg>
    <div><b>35</b><span>Touchdowns</span></div>
  </div>
  <div class="abs stat" style="left:645px">
    <svg width="58" height="54" viewBox="0 0 58 54"><circle cx="26" cy="7" r="5" fill="#1b1b1b"/><path d="M26 14l-4 16 8 8v14M22 30l-10 20M26 18l12 6M4 22l44 28" fill="none" stroke="#1b1b1b" stroke-width="3"/></svg>
    <div><b>40</b><span>Teammembers</span></div>
  </div>
  <div class="abs stat" style="left:925px">
    <svg width="56" height="54" viewBox="0 0 56 54"><path d="M16 4h24v14a12 12 0 0 1-24 0zM16 8H6c0 10 6 14 10 14M40 8h10c0 10-6 14-10 14M28 30v12M16 50h24v-8H16z" fill="none" stroke="#1b1b1b" stroke-width="3"/></svg>
    <div><b>10</b><span>Awards Won</span></div>
  </div>
</section>

<section>
  <div class="abs prod-title"><h2 class="heading"><span class="hl">TOP PRODUCTS</span> &amp; MERCHANDICE</h2><div class="underline"></div></div>
  <p class="abs prod-text">Official club gear for players, parents and fans. Every purchase supports ice time, coaching and equipment for our youth teams. Browse gloves, keychains and fan items below, with new pieces added every season.</p>
  <article class="abs product" style="left:98px">
    <div class="abs img" role="img" aria-label="Product photo of a glove keychain"></div>
    <div class="abs pname">PRODUCT NAME</div>
    <div class="abs bar"><span>ADD TO CART</span><span class="price">$199</span></div>
  </article>
  <article class="abs product" style="left:355px">
    <div class="abs img" role="img" aria-label="Product photo of a black and yellow hockey glove"></div>
    <div class="abs pname">PRODUCT NAME</div>
    <div class="abs bar"><span>ADD TO CART</span><span class="price">$199</span></div>
  </article>
  <article class="abs product" style="left:612px">
    <div class="abs img" role="img" aria-label="Product photo of a hockey glove side view"></div>
    <div class="abs pname">PRODUCT NAME</div>
    <div class="abs bar"><span>ADD TO CART</span><span class="price">$199</span></div>
  </article>
  <article class="abs product" style="left:870px">
    <div class="abs img" role="img" aria-label="Product image of a club emblem sticker"></div>
    <div class="abs pname">PRODUCT NAME</div>
    <div class="abs bar"><span>ADD TO CART</span><span class="price">$199</span></div>
  </article>
</section>

<section class="abs partners">
  <h2 class="heading"><span class="hl">MEET OUR</span> PARTNERS</h2>
  <p class="sub">Our best friends ever</p>
  <div class="underline"></div>
  <div class="abs plogo" style="left:98px">Logo Here</div>
  <div class="abs plogo" style="left:266px">Logo Here</div>
  <div class="abs plogo" style="left:434px">Logo Here</div>
  <div class="abs plogo" style="left:602px">Logo Here</div>
  <div class="abs plogo" style="left:770px">Logo Here</div>
  <div class="abs plogo" style="left:938px">Logo Here</div>
  <div class="abs hero-dots"><b></b><b></b><b></b></div>
</section>

<section>
  <div class="abs news-title"><h2 class="heading"><span class="hl">LATEST</span> NEWS</h2><div class="underline"></div></div>
  <div class="abs news-main" role="img" aria-label="Photo of a youth field hockey player running with the ball"></div>
  <div class="abs" style="left:98px;top:2778px">
    <div class="date" style="font-size:17px">Monday, December 19th</div>
    <div class="ntitle" style="font-size:30px;margin:4px 0 12px">Game Highlights: Splashes at Comets</div>
    <div class="meta"><span>▭ &nbsp;Analysis</span><span>◯ &nbsp;0</span></div>
  </div>
  <article class="abs news-item" style="top:2490px">
    <div class="abs thumb" role="img" aria-label="News thumbnail photo of a player"></div>
    <div class="abs txt"><div class="date" style="font-size:11px">Monday, December 19th</div><div class="ntitle">Game Highlights: Splashes at Comets</div><div class="meta" style="font-size:10px;margin-top:6px"><span>Analysis</span><span>0</span></div></div>
  </article>
  <article class="abs news-item" style="top:2625px">
    <div class="abs thumb" role="img" aria-label="News thumbnail photo of a player"></div>
    <div class="abs txt"><div class="date" style="font-size:11px">Monday, December 19th</div><div class="ntitle">Game Highlights: Splashes at Comets</div><div class="meta" style="font-size:10px;margin-top:6px"><span>Analysis</span><span>0</span></div></div>
  </article>
  <article class="abs news-item" style="top:2760px;border:0">
    <div class="abs thumb" role="img" aria-label="News thumbnail photo of a player"></div>
    <div class="abs txt"><div class="date" style="font-size:11px">Monday, December 19th</div><div class="ntitle">Game Highlights: Splashes at Comets</div><div class="meta" style="font-size:10px;margin-top:6px"><span>Analysis</span><span>0</span></div></div>
  </article>
</section>

<footer class="abs footer">
  <div class="abs name">HORNETS</div>
  <p class="abs f-about">A youth hockey club built on teamwork, respect and hard work on the ice. We train young players of every level and help them grow as athletes and teammates.</p>
  <div class="abs f-col" style="left:413px;top:118px">
    <h4>QUICK <span>LINKS</span></h4>
    <ul><li>Home</li><li>News</li><li>Team</li><li>Club</li><li>Partners</li><li>Contact</li><li>Shop</li></ul>
  </div>
  <div class="abs f-col" style="left:545px;top:118px">
    <h4>NEW <span>PRODUCTS</span></h4>
    <ul class="bul"><li>Junior practice jersey, home colours</li><li>Training gloves with extra padding</li><li>Club keychain with mini glove</li><li>Warm winter beanie for fans</li><li>Team water bottle, one litre</li><li>Kids hoodie with club crest</li></ul>
  </div>
  <div class="abs f-col contact" style="left:850px;top:118px">
    <h4>CONTACT <span>US</span></h4>
    <ul>
      <li><svg width="10" height="14" viewBox="0 0 10 14"><path d="M5 14S0 8 0 5a5 5 0 0 1 10 0c0 3-5 9-5 9z" fill="#fbc52d"/></svg><span>PO BOX 212 MAPLE RIDGE<br>NORTH RINK, MAIN ENTRANCE</span></li>
      <li><svg width="12" height="12" viewBox="0 0 12 12"><path d="M2 0l3 3-2 2a7 7 0 0 0 4 4l2-2 3 3-2 2C5 12 0 7 0 2z" fill="#fbc52d"/></svg><span>(555) 014-7720</span></li>
      <li><svg width="12" height="9" viewBox="0 0 12 9"><rect width="12" height="9" fill="#fbc52d"/><path d="M0 0l6 5 6-5" fill="none" stroke="#232323"/></svg><span>info@hornets.club</span></li>
    </ul>
  </div>
  <div class="abs f-social"><i class="dot"></i><i class="dot"></i><i class="dot"></i><i class="dot"></i></div>
</footer>
<div class="abs copy">© 2017 Hornets Hockey Youth Club. &nbsp;|&nbsp; All Rights Reserved.</div>

</body>
</html>
```